Young, dynamic furniture company requires leaflet design

We require a new leaflet for our modern furniture company which supplies furniture and appliances to the property and development market.
Bramwell Furniture has become one of the leading furniture & appliance suppliers to the property market withing London. With over 10 years experience, we have increased our business to supply not only Private Landlords and Managing Agents, but also Property Developers, Housing Associations and Local Councils.
We offer not only a complete range of furniture which includes beds, wardrobes, dining sets and sofas, but also a high quality, full delivery and assembly service to help you with all our furnishing needs.

Target Market(s)

Private Landlords, Developers, Letting & Managing Agents

Industry/Entity Type

Furniture Store

Font styles to use
Sans Serif

Colors
0255a3
3176b5
85abd2
cfdeed
eaf1f7

Requirements
Must have
• Contact details,
• Our services:
• FREE next day delivery within the M25
• Free furniture assembly
• Free key pick up & drop off
• Free furniture removal (on a like-for-like basis)
• All types of furniture supplied - from basic to luxury

```html
<!DOCTYPE html>
<html lang="en">
<head>
<meta charset="utf-8">
<title>Bramwell Furniture – Our Services</title>
<link href="https://fonts.googleapis.com/css2?family=Lato:wght@300;400;700;900&display=swap" rel="stylesheet">
<style>
  :root {
    --brand-blue: #2c62a3;
    --ring-blue: #3176b5;
    --navy: #35325a;
    --ink: #0d0d12;
    --paper: #ffffff;
  }
  html, body {
    margin: 0;
    padding: 0;
    overflow: hidden;
    background: var(--paper);
  }
  .leaflet {
    position: relative;
    width: 1041px;
    height: 1200px;
    overflow: hidden;
    background: var(--paper);
    font-family: "Lato", Arial, sans-serif;
    color: var(--ink);
  }
  .leaflet__shapes {
    position: absolute;
    inset: 0;
  }
  .brand {
    position: absolute;
    left: 118px;
    top: 165px;
    display: flex;
    align-items: center;
    gap: 14px;
  }
  .brand__dot {
    width: 30px;
    height: 30px;
    border-radius: 50%;
    background: var(--brand-blue);
  }
  .brand__name {
    font-weight: 900;
    font-size: 38px;
    color: var(--navy);
    letter-spacing: 0.5px;
    white-space: nowrap;
  }
  .services__heading {
    position: absolute;
    left: 78px;
    top: 420px;
    margin: 0;
    font-weight: 900;
    font-size: 53px;
    letter-spacing: 0.5px;
  }
  .service {
    position: absolute;
    margin: 0;
  }
  .service__head {
    display: flex;
    align-items: baseline;
    gap: 18px;
  }
  .service__number {
    font-weight: 900;
    font-size: 70px;
    line-height: 1;
    color: var(--navy);
  }
  .service__title {
    font-weight: 900;
    font-size: 29px;
    line-height: 1;
  }
  .service__desc {
    margin: 8px 0 0 5px;
    font-size: 17.5px;
    font-weight: 400;
  }
  .service--1 { left: 105px; top: 498px; }
  .service--2 { left: 153px; top: 631px; }
  .service--3 { left: 214px; top: 755px; }
  .service--4 { left: 296px; top: 872px; }

  .range-statement {
    position: absolute;
    right: 26px;
    top: 478px;
    margin: 0;
    text-align: right;
    font-weight: 900;
    font-size: 53px;
    line-height: 50px;
  }
  .range-statement__light {
    font-weight: 300;
  }
  .contact {
    position: absolute;
    left: 772px;
    top: 1064px;
    font-weight: 900;
    font-size: 21px;
    line-height: 26px;
    white-space: nowrap;
  }
  .contact__icons {
    display: flex;
    gap: 12px;
    margin-bottom: 6px;
  }
  .contact__line { display: block; }
</style>
</head>
<body>
<main class="leaflet">
  <svg class="leaflet__shapes" width="1041" height="1200" viewBox="0 0 1041 1200" aria-hidden="true">
    <path d="M446 0 L1041 0 L1041 410 C990 380 940 350 880 345 L700 330 L560 170 C530 110 500 50 446 0 Z" fill="var(--brand-blue)"/>
    <path d="M0 218 C60 330 200 375 320 367 C410 362 470 340 514 312" fill="none" stroke="var(--brand-blue)" stroke-width="11"/>
    <circle cx="689" cy="307" r="165" fill="var(--paper)"/>
    <circle cx="689" cy="307" r="150" fill="var(--ring-blue)"/>
    <circle cx="689" cy="307" r="138" fill="var(--paper)"/>
    <circle cx="689" cy="307" r="128" fill="var(--navy)"/>
    <path d="M0 1026 C90 1055 150 1068 260 1060 C340 1050 360 1014 430 1012 C560 1010 680 1080 743 1200 L0 1200 Z" fill="var(--brand-blue)"/>
  </svg>

  <div class="brand">
    <span class="brand__dot"></span>
    <span class="brand__name">Bramwell Furniture</span>
  </div>

  <h2 class="services__heading">OUR SERVICES:</h2>

  <div class="service service--1">
    <div class="service__head"><span class="service__number">01</span><span class="service__title">FREE DELIVERY</span></div>
    <p class="service__desc">FREE next day delivery within the M25</p>
  </div>
  <div class="service service--2">
    <div class="service__head"><span class="service__number">02</span><span class="service__title">FREE ASSEMBLY</span></div>
    <p class="service__desc">Free furniture assembly</p>
  </div>
  <div class="service service--3">
    <div class="service__head"><span class="service__number">03</span><span class="service__title">FREE PICK UP &amp; DROP OFF</span></div>
    <p class="service__desc">Free key pick up &amp; drop off</p>
  </div>
  <div class="service service--4">
    <div class="service__head"><span class="service__number">04</span><span class="service__title">FREE FURNITURE REMOVAL</span></div>
    <p class="service__desc">Free furniture removal (on a like-for-like basis)</p>
  </div>

  <p class="range-statement">
    ALL TYPES OF<br>
    FURNITURE<br>
    <span class="range-statement__light">SUPPLIED -</span><br>
    FROM BASIC<br>
    TO LUXURY
  </p>

  <div class="contact">
    <div class="contact__icons">
      <svg width="32" height="32" viewBox="0 0 32 32" aria-label="Phone">
        <rect width="32" height="32" rx="5" fill="var(--ink)"/>
        <path d="M11 7 C9 8 8 10 9 13 C11 19 14 22 19 24 C22 25 24 24 25 22 L22 19 L19 21 C16 19 14 17 12 14 L14 11 Z" fill="var(--paper)"/>
      </svg>
      <svg width="32" height="32" viewBox="0 0 32 32" aria-label="Website">
        <g fill="none" stroke="var(--ink)" stroke-width="1.6">
          <circle cx="16" cy="16" r="13"/>
          <ellipse cx="16" cy="16" rx="6" ry="13"/>
          <line x1="3" y1="16" x2="29" y2="16"/>
          <path d="M5 9 H27 M5 23 H27"/>
          <line x1="16" y1="3" x2="16" y2="29"/>
        </g>
      </svg>
    </div>
    <span class="contact__line">020 7946 0321</span>
    <span class="contact__line">www.bramwell.co.uk</span>
  </div>
</main>
</body>
</html>
```